An innovative software company needs a business card!

We need a business card design for our new innovative software company. Please use the details for the business card provided in business card details section. We will use the business card paper like: https://www.plavex.com/us/products/nfc/business-cards-plus.html Our company name: kelvora We have already a logo and colors to use in business cards too ,

Target Market(s)

App & Sofware Development

Industry/Entity Type

Software

Contact Information for Business Card

Lukas Brenner, BSc.
Owner and Creative Superhero

Adress:
Tulpenweg 37/4/1809
A - 1100, Wien

Tel: +43 (0) 676 921 35 60
Email: lukas.brenner@kelvora.at
Web: www.kelvora.at

Requirements
Must have
• - Use our logo
Nice to have
• It would be nice to have a nice picture on the backside. (About apps, software, technicals or funy stuff) - Use our colors as in business card (optional)

```html
<!DOCTYPE html>
<html lang="en">
<head>
<meta charset="utf-8">
<title>kelvora – business card</title>
<link rel="stylesheet" href="https://fonts.googleapis.com/css2?family=Questrial&display=swap">
<style>
  :root {
    --page-bg: #c9ced1;
    --card-white: #ffffff;
    --panel-grey: #cbcccf;
    --brand-blue: #1fa3d1;
    --brand-blue-light: #7cc3e2;
    --text-grey: #4a4a4a;
    --faint-circle: #eef2f5;
  }
  * { margin: 0; padding: 0; box-sizing: border-box; }
  html, body {
    width: 1055px; height: 1200px; overflow: hidden;
    background: var(--page-bg);
    font-family: "Questrial", "Century Gothic", sans-serif;
  }
  .card {
    position: absolute; left: 202px; width: 650px; height: 406px; overflow: hidden;
  }
  .card-front { top: 170px; background: var(--card-white); }
  .card-back { top: 649px; height: 402px; background: var(--brand-blue); }

  .brand-panel {
    position: absolute; left: 0; top: 0; width: 172px; height: 100%;
    background: var(--panel-grey);
  }
  .brand-name {
    position: absolute; left: 94px; top: 150px;
    transform: translate(-50%, -50%) rotate(-90deg);
    font-size: 64px; color: var(--brand-blue); line-height: 1; white-space: nowrap;
    letter-spacing: 1px;
  }
  .brand-dot {
    position: absolute; left: 72px; top: 290px; width: 44px; height: 44px;
    border-radius: 50%; background: var(--brand-blue);
  }
  .faint-circle {
    position: absolute; left: 458px; top: 70px; width: 300px; height: 300px;
    border-radius: 50%; background: var(--faint-circle);
  }

  .info-block {
    position: absolute; left: 172px; padding-left: 23px;
    color: var(--text-grey); font-size: 17px; line-height: 20px;
  }
  .info-block::before {
    content: ""; position: absolute; left: 0; top: 0; width: 16px; height: 100%;
    background: var(--brand-blue);
  }
  .info-name { top: 108px; }
  .person-name { color: var(--brand-blue); font-size: 18px; letter-spacing: 0.5px; }
  .info-address { top: 178px; padding-left: 26px; }
  .info-contact { top: 253px; padding-left: 26px; }
  .contact-line { display: flex; align-items: center; gap: 8px; }
  .contact-line svg { width: 17px; height: 17px; flex: none; }

  .back-illustration {
    position: absolute; left: 360px; top: 40px; width: 290px; height: 362px;
    background: linear-gradient(160deg, #e9eef2 0%, #d4dde3 55%, #a9d4c3 100%);
    opacity: 0.55;
  }
</style>
</head>
<body>
  <section class="card card-front">
    <div class="faint-circle" aria-hidden="true"></div>
    <div class="brand-panel">
      <div class="brand-name">kelvora</div>
      <div class="brand-dot" aria-hidden="true"></div>
    </div>

    <div class="info-block info-name">
      <div class="person-name">LUKAS BRENNER, BSC.</div>
      <div class="person-role">Owner and Creative Superhero</div>
    </div>

    <div class="info-block info-address">
      <div>Tulpenweg 37/4/1809</div>
      <div>A - 1100, Wien</div>
    </div>

    <div class="info-block info-contact">
      <div class="contact-line">
        <svg viewBox="0 0 16 16" aria-hidden="true"><rect x="0" y="0" width="16" height="16" rx="3" fill="#1fa3d1"/><path d="M5 3.5l2 2-1 1.3c.6 1.3 1.6 2.3 2.9 2.9l1.3-1 2 2-1.2 1.8C7.6 12.2 3.8 8.4 3.5 4.7z" fill="#fff"/></svg>
        <span>+43 (0) 676 921 35 60</span>
      </div>
      <div class="contact-line">
        <svg viewBox="0 0 16 16" aria-hidden="true"><rect x="1" y="3.5" width="14" height="9" fill="#1fa3d1"/><path d="M1 3.5l7 5 7-5M1 12.5l5-4.5M15 12.5l-5-4.5" stroke="#fff" stroke-width="1" fill="none"/></svg>
        <span>lukas.brenner@kelvora.at</span>
      </div>
      <div class="contact-line">
        <svg viewBox="0 0 16 16" aria-hidden="true"><g fill="none" stroke="#1fa3d1" stroke-width="1"><circle cx="8" cy="8" r="6.5"/><ellipse cx="8" cy="8" rx="3" ry="6.5"/><path d="M1.5 8h13M2.5 4.8h11M2.5 11.2h11"/></g></svg>
        <span>www.kelvora.at</span>
      </div>
    </div>
  </section>

  <section class="card card-back">
    <div class="back-illustration" role="img" aria-label="Flat illustration of a desk seen from above: laptop, documents with charts, glasses, pen, coffee cup and working hands"></div>
  </section>
</body>
</html>
```